Wordpress Design Project for Bankruptcy Law Office in San Francisco

our current website: www.dorvanelilaw.example

we would like to re-design it for wordpress to make it faster and a bit more modern.

content should be similar to what we have there right now but also we do family law

please include logo for law office:

Law Office of Marta K. Dorvaneli

Thank you.
Updates

please see attached word document with logos that we like as an example.

we do tend to like color red.  darker red.

Please submit your design variations and logo as soon as possible.   We would like to go over them and make our decision

Reason: Please create couple of more variations of logo for your design, so we can make our decision what we like the most. Please see word doc for samples: Text: Law Office Of Marta K. Dorvaneli

Reason: final touches

Target Market(s)

bankruptcy and family law clients

Industry/Entity Type

Family Law

Requirements
Must have
• see examples of law sites
http://marketing.lexoriba.example/testimonials

- new logo: Law Office of Marta K. Dorvaneli
- client intake form
- blog
- contact us form

Nice to have
• - map
- red color
- on the front page a nice photo of SF or a happy family

```html
<!DOCTYPE html>
<html lang="en">
<head>
<meta charset="utf-8">
<title>Law Office of Marta K. Dorvaneli</title>
<link href="https://fonts.googleapis.com/css2?family=Cinzel:wght@400;700&family=Open+Sans:wght@400;600;700&family=Oswald:wght@300;400&display=swap" rel="stylesheet">
<style>
:root{
  --cream:#fcf3e2;
  --orange-dark:#c8501a;
  --orange-light:#ff7b30;
  --gold:#f6b233;
  --gold-dark:#d99a1c;
  --teal:#1e5e4f;
  --teal-dark:#0e4438;
  --heading:#1f5e4a;
  --text:#808080;
  --ink:#3a4a45;
  --red:#b13c40;
  --panel:#e4dfd4;
}
*{margin:0;padding:0;box-sizing:border-box}
html,body{width:919px;height:1200px;overflow:hidden}
body{position:relative;background:var(--cream);font-family:Arial,Helvetica,sans-serif}
.abs{position:absolute}

.site-header{left:0;top:0;width:919px;height:102px;background:radial-gradient(ellipse at 20% 40%,#fffdf8 0%,#fbf2df 60%,#f8eed9 100%)}
.brand{left:58px;top:38px;display:flex;align-items:center;gap:10px}
.brand-square{width:22px;height:22px;background:var(--orange-dark)}
.brand-name{font-family:'Open Sans',sans-serif;font-weight:400;font-size:18px;color:var(--ink);white-space:nowrap}
.social{right:37px;top:44px;display:flex;gap:5px}
.social span{width:21px;height:21px;background:#3b3b3b;border-radius:3px}
.call{right:37px;top:76px;font-family:'Open Sans',sans-serif;font-size:17px;color:#111}

.hero-band{left:0;top:102px;width:919px;height:398px;background:linear-gradient(#f6b233 0 8px,var(--orange-dark) 8px,var(--orange-light) 390px,#ffb356 390px)}
.main-nav{left:0;top:134px;width:919px;height:24px;font-family:'Open Sans',sans-serif;font-size:16.5px;color:#fff}
.main-nav a{position:absolute;color:#fff;text-decoration:none}
.slider{left:60px;top:163px;width:809px;height:304px;border:9px solid var(--gold);background:linear-gradient(100deg,#5a5a58 0%,#8c8c88 20%,#3a3b40 45%,#55565a 70%,#2c2d33 100%)}
.slide-caption{left:94px;top:188px;font-family:'Oswald',sans-serif;font-weight:300;font-size:39px;color:#fff;white-space:nowrap;text-shadow:2px 2px 0 rgba(120,60,20,.7)}
.slide-caption b{font-weight:400;font-size:56px;letter-spacing:1px}
.arrow{top:293px;width:40px;height:40px}

.feature{top:520px;width:261px}
.feature h2{font-family:'Cinzel',serif;font-weight:400;font-size:16px;color:var(--heading);white-space:nowrap;height:40px}
.feature .photo{height:101px;border:3px solid var(--teal)}
.feature p{margin-top:15px;font-size:11.2px;line-height:17px;color:var(--text);text-align:justify}
.btn{display:flex;width:110px;height:33px;border:3px solid #fff;box-shadow:0 0 0 1px #d8d0c0;font-family:'Open Sans',sans-serif;font-weight:700;font-size:12.5px;color:#fff}
.btn .more{flex:1;background:linear-gradient(#2f8a70,#1b5c4a);display:flex;align-items:center;justify-content:center;text-shadow:0 1px 1px #0b3328}
.btn .go{width:24px;background:linear-gradient(#f7c34a,#e09a1c);display:flex;align-items:center;justify-content:center}

.divider{height:1px;background:#ddd3c2}
.info{left:60px;top:818px;width:536px}
.info h2{font-family:'Cinzel',serif;font-weight:400;font-size:22px;color:var(--heading);letter-spacing:.5px}
.info p{margin-top:16px;font-size:13.1px;line-height:22.5px;color:var(--text);text-align:justify;hyphens:auto;-webkit-hyphens:auto}
.info p + p{margin-top:22px}

.contact-panel{left:611px;top:806px;width:259px;height:298px;background:var(--panel);border:2px solid #d5cfc1;clip-path:polygon(14px 0,calc(100% - 14px) 0,100% 14px,100% calc(100% - 14px),calc(100% - 14px) 100%,14px 100%,0 calc(100% - 14px),0 14px)}
.contact-title{left:644px;top:805px;width:191px;height:42px;background:linear-gradient(#d8ce6e,#b9ad3a);font-family:'Cinzel',serif;font-size:17px;letter-spacing:1px;color:#fff;display:flex;align-items:center;justify-content:center}
.field{left:627px;width:228px;background:var(--red);font-family:Georgia,serif;font-weight:700;font-size:10px;color:#fff;padding:2px 8px;letter-spacing:.5px}
.submit{left:709px;top:1069px;width:64px;height:20px;background:linear-gradient(#f8d6cb,#e9a896);font-family:Georgia,serif;font-size:8px;font-weight:700;letter-spacing:1px;color:#7a2a28;display:flex;align-items:center;justify-content:center}

.site-footer{left:0;top:1145px;width:919px;height:55px;background:var(--teal-dark);color:#fff;font-size:11.5px;padding:20px 0 0 62px}
</style>
</head>
<body>

<header class="site-header abs">
  <div class="brand abs">
    <span class="brand-square"></span>
    <span class="brand-name">Law Office of Marta K. Dorvaneli</span>
  </div>
  <div class="social abs"><span></span><span></span><span></span></div>
  <div class="call abs">Call Us Now : 000-000-000</div>
</header>

<div class="hero-band abs"></div>
<nav class="main-nav abs">
  <a href="#" style="left:65px">HOME</a>
  <a href="#" style="left:156px">ABOUT US</a>
  <a href="#" style="left:273px">AREAS OF PRACTICE</a>
  <a href="#" style="left:462px">RESOURCES</a>
  <a href="#" style="left:598px">BLOG</a>
  <a href="#" style="left:687px">FAQ</a>
  <a href="#" style="left:769px">CONTACT US</a>
</nav>

<div class="slider abs" role="img" aria-label="Photo of four smiling attorneys in suits standing before courthouse columns">
  <div class="slide-caption abs">We offer our clients an expert <b>LEGAL</b> advice.</div>
</div>
<svg class="arrow abs" style="left:21px" viewBox="0 0 40 40"><circle cx="20" cy="20" r="20" fill="#aaa58d"/><path d="M23 12l-8 8 8 8" stroke="#fff" stroke-width="3" fill="none"/></svg>
<svg class="arrow abs" style="left:857px" viewBox="0 0 40 40"><circle cx="20" cy="20" r="20" fill="#aaa58d"/><path d="M17 12l8 8-8 8" stroke="#fff" stroke-width="3" fill="none"/></svg>

<section class="feature abs" style="left:60px">
  <h2>More Than Just a Lawyer</h2>
  <div class="photo" role="img" aria-label="Photo of a team of four attorneys" style="background:linear-gradient(90deg,#8d8c88,#3c3d45 40%,#6f6e6a 70%,#2d2e36)"></div>
  <p>Lorem ipsum dolor sit amet, consectetuer adipiscing elit, sed diam nonummy nibh euismod tincidunt ut laoreet dolore magna aliquam erat volutpat.</p>
  <div class="btn" style="margin:17px 0 0 151px"><span class="more">Read More</span><span class="go">GO</span></div>
</section>

<section class="feature abs" style="left:336px">
  <h2>Free Attorney Consultation</h2>
  <div class="photo" role="img" aria-label="Photo of a barrister's wig resting on law books" style="background:linear-gradient(90deg,#3a2418,#c9a774 40%,#d9c08d 60%,#2a3a24)"></div>
  <p>Lorem ipsum dolor sit amet, consectetuer adipiscing elit, sed diam nonummy nibh euismod tincidunt ut laoreet dolore magna aliquam erat volutpat.</p>
  <div class="btn" style="margin:17px 0 0 149px"><span class="more">Read More</span><span class="go">GO</span></div>
</section>

<section class="feature abs" style="left:610px">
  <h2>Understand the Alternatives</h2>
  <div class="photo" role="img" aria-label="Photo of two businessmen reviewing a document in a bright office" style="background:linear-gradient(90deg,#eef0f1,#3d3f45 35%,#e2e4e6 55%,#2f3137 75%,#f2f3f4)"></div>
  <p>Lorem ipsum dolor sit amet, consectetuer adipiscing elit, sed diam nonummy nibh euismod tincidunt ut laoreet dolore magna aliquam erat volutpat.</p>
  <div class="btn" style="margin:17px 0 0 152px"><span class="more">Read More</span><span class="go">GO</span></div>
</section>

<div class="divider abs" style="left:60px;top:788px;width:536px"></div>
<div class="divider abs" style="left:610px;top:788px;width:260px"></div>

<section class="info abs" lang="en">
  <h2>Important Information</h2>
  <p>The Law Offices of Marta K. Dorvaneli is a consumer law office dedicated to consumer protection and zealously defending the rights of our clients.&nbsp; We offer the big firm quality legal representation with a small firm individualized attention to each client.</p>
  <p>Our office offers services in: all types of consumer bankruptcy filings, i.e. Chapter 7, Chapter 13, Chapter 11, negotiating a settlement of your debts, assisting you in the defense of collection litigation and defending you against foreclosure. Please review our site and see what we may be able to offer you. Feel free to call us at (415) 555-0148 or use our free case evaluation form.</p>
  <div class="btn" style="margin:14px 0 0 424px"><span class="more">Read More</span><span class="go">GO</span></div>
</section>

<aside>
  <div class="contact-panel abs"></div>
  <div class="contact-title abs">CONTACT FORM</div>
  <div class="field abs" style="top:882px;height:18px">Name:</div>
  <div class="field abs" style="top:909px;height:18px">E-mail:</div>
  <div class="field abs" style="top:935px;height:18px">Phone:</div>
  <div class="field abs" style="top:961px;height:18px">Subject:</div>
  <div class="field abs" style="top:982px;height:63px">Message:</div>
  <div class="divider abs" style="left:627px;top:1057px;width:228px;background:#f0c9c0"></div>
  <div class="submit abs">SUBMIT</div>
</aside>

<footer class="site-footer abs">copyright@2012.All rights reserved.</footer>

</body>
</html>
```